Banner Design for High End Jewelry Website

We need a banner for our website (brindlestone.com) for a sale that we will be running. The banner should be a size 1187 × 400. I have included a few pieces of jewelry to be included in the banner (do not need to use all, can use just some). The banner should say:
"Christmas is Closer Than You Think Sale!"
Shop Now

Industry/Entity Type

Jewelry

```html
<!DOCTYPE html>
<html lang="en">
<head>
<meta charset="utf-8">
<title>Christmas Sale Banner</title>
<link rel="stylesheet" href="https://fonts.googleapis.com/css2?family=Yanone+Kaffeesatz:wght@600&family=Sansita:ital,wght@1,800&display=swap">
<style>
  :root {
    --backdrop: #4d4d4d;
    --festive-red: #e30000;
    --sale-yellow: #ffe600;
    --snow-white: #ffffff;
    --arc-grey: #b3b3b8;
    --divider-red: #c8101a;
    --gold-light: #f2d27a;
    --gold-deep: #b8862c;
  }
  * { margin: 0; padding: 0; box-sizing: border-box; }
  html, body {
    width: 1200px;
    height: 670px;
    overflow: hidden;
    background: var(--backdrop);
  }
  .sale-banner {
    position: absolute;
    left: 126px;
    top: 175px;
    width: 949px;
    height: 320px;
    background: var(--snow-white);
    overflow: hidden;
  }
  .banner-shape {
    position: absolute;
    inset: 0;
    width: 949px;
    height: 320px;
  }
  .snowflake {
    position: absolute;
    border-radius: 50%;
    background: radial-gradient(circle, var(--snow-white) 0%, rgba(255,255,255,0.85) 45%, rgba(255,255,255,0) 72%);
  }
  .snowflake--top { left: 137px; top: 0px; width: 70px; height: 70px; }
  .snowflake--bottom { left: 218px; top: 245px; width: 50px; height: 50px; }
  .sale-message {
    position: absolute;
    left: 44px;
    top: 78px;
    width: 440px;
    transform: rotate(-5deg);
    transform-origin: center;
    text-align: center;
  }
  .sale-headline {
    font-family: "Yanone Kaffeesatz", "Arial Narrow", sans-serif;
    font-weight: 600;
    font-size: 50px;
    line-height: 42px;
    color: var(--sale-yellow);
    letter-spacing: 0.2px;
  }
  .shop-now {
    display: inline-block;
    margin-top: 4px;
    font-family: "Sansita", "Georgia", serif;
    font-style: italic;
    font-weight: 800;
    font-size: 70px;
    line-height: 80px;
    color: var(--snow-white);
    text-decoration: none;
  }
  .product-photo {
    position: absolute;
    border-radius: 40%;
  }
  .product-photo--gemstone-ring {
    left: 488px; top: 113px; width: 118px; height: 116px;
    background: radial-gradient(circle at 50% 45%, #5b7a8a 0%, #6a6f5a 35%, var(--gold-deep) 62%, rgba(255,255,255,0) 75%);
  }
  .product-photo--flower-ring {
    left: 640px; top: 113px; width: 120px; height: 112px;
    background: radial-gradient(circle at 50% 50%, #9a3050 0%, #c9a452 22%, #6b6656 55%, rgba(255,255,255,0) 74%);
  }
  .product-photo--scale-ring {
    left: 800px; top: 113px; width: 110px; height: 104px;
    background: radial-gradient(circle at 50% 50%, var(--gold-light) 0%, #d6a53e 45%, var(--gold-deep) 60%, rgba(255,255,255,0) 74%);
  }
  .product-divider {
    position: absolute;
    top: 99px;
    width: 2px;
    height: 132px;
    background: var(--divider-red);
  }
  .product-divider--first { left: 622px; }
  .product-divider--second { left: 779px; }
</style>
</head>
<body>
  <section class="sale-banner">
    <svg class="banner-shape" viewBox="0 0 949 320" aria-hidden="true">
      <path d="M0 0 L526 0 Q412 170 490 320 L0 320 Z" fill="var(--arc-grey)"/>
      <path d="M0 0 L512 0 Q400 160 464 320 L0 320 Z" fill="var(--festive-red)"/>
    </svg>

    <div class="snowflake snowflake--top" role="img" aria-label="White snowflake ornament"></div>
    <div class="snowflake snowflake--bottom" role="img" aria-label="Small white snowflake ornament"></div>

    <div class="sale-message">
      <h1 class="sale-headline">"Christmas is Closer<br>Than You Think Sale!"</h1>
      <a class="shop-now" href="#">Shop Now</a>
    </div>

    <div class="product-photo product-photo--gemstone-ring" role="img" aria-label="Photo of a gold ring set with cabochon sapphires, emeralds and rubies"></div>
    <span class="product-divider product-divider--first"></span>
    <div class="product-photo product-photo--flower-ring" role="img" aria-label="Photo of a gold floral ring with a central ruby and diamonds"></div>
    <span class="product-divider product-divider--second"></span>
    <div class="product-photo product-photo--scale-ring" role="img" aria-label="Photo of a gold scale-pattern band ring with pavé diamonds"></div>
  </section>
</body>
</html>
```